Need new website for my business

I want to design a new Irrigation website for our business. What we are looking for is to have a residential section that describes providing for irrigation service for residential customers in homeowners Association. From startups to service to winterization in full residential installs.
A commercial section on our webpage describing. installation of commercial Irrigation systems. Service start-up of systems. To winterizations. Offering contract service plans for commercial customers.
Service for both commercial residential include making sure all zones are operating check for leaks adjust spray nozzles in rotors making sure all irrigation heads rotate, and are not stuck or damaged making sure that we have full coverage of each Irrigation zone for lawns. In all drip irrigation is Functioning in watering the plants accordingly. Adjusting control settings to make sure you have the right watering times during the hot dry months.
Have a landscape lighting tab:
Describing what landscape lighting and what it does to enhance curb, appeal, highlight architectural, features of landscape and transferring your outdoor space into inviting visual stunning areas with low-voltage landscape lighting
And a residential snow plowing for the Falmouth Maine area. In commercial snow, plowing and snow removal covering Scarborough south portland Portland Falmouth in Cumberland Maine for commercial Snow services. From plow & Salting parking lots to Snow removing, and Snow displacement.
we started a website but it needs a up lift and bring it to pop
our web site is bluefinchyardworks311.com
here are a few websites that we really like:
www.wetlandsprayco.com
www.dewpointsprinkler.com
www.mellowmeadowwatering.com
Industry/Entity Type
Irrigation & Landscape Lighting
Coding
Coded - Design and coding required
Number of Pages Required
4 page
Font styles to use
Look and feel
Each slider illustrates characteristics of the customer's brand and the style your logo design should communicate.

```html
<!DOCTYPE html>
<html lang="en">
<head>
<meta charset="UTF-8">
<title>Bluefinch Irrigation &amp; Lighting</title>
<link rel="stylesheet" href="https://fonts.googleapis.com/css2?family=Open+Sans:wght@400;600;700&family=Source+Serif+4:wght@500;600&display=swap">
<style>
  :root {
    --navy: #0e2a47;
    --white: #ffffff;
    --ink: #1f2a36;
    --muted: #4a5663;
    --brand-green: #3d9a3a;
    --accent-blue: #1e7fcf;
    --accent-blue-dark: #1567b0;
    --nav-link: #2c5f8f;
    --para-light: #c9d3de;
    --hero-light: #5f7a5a;
    --hero-dark: #3d6330;
  }
  * { box-sizing: border-box; margin: 0; padding: 0; }
  html, body {
    width: 1200px;
    height: 618px;
    overflow: hidden;
  }
  body {
    font-family: "Open Sans", Arial, sans-serif;
    background: var(--navy);
    position: relative;
  }
  .site-header {
    position: absolute;
    left: 0; top: 0;
    width: 1200px; height: 57px;
    background: var(--white);
  }
  .brand-name {
    position: absolute;
    left: 143px; top: 12px;
    font-size: 27px;
    font-weight: 700;
    color: var(--brand-green);
    letter-spacing: -0.5px;
  }
  .nav-home {
    position: absolute;
    left: 585px; top: 19px;
    font-size: 16px;
    color: var(--ink);
  }
  .nav-links {
    position: absolute;
    right: 133px; top: 22px;
    display: flex;
    gap: 26px;
    font-size: 12px;
    color: var(--nav-link);
  }
  .content-column {
    position: absolute;
    left: 139px; top: 60px;
    width: 574px; height: 558px;
    background: var(--white);
  }
  .hero-photo {
    position: absolute;
    left: 0; top: 0;
    width: 574px; height: 298px;
    background: linear-gradient(180deg, var(--hero-light) 0%, var(--hero-dark) 100%);
  }
  .feature-ticks {
    position: absolute;
    left: 51px; top: 189px;
    display: flex;
    gap: 51px;
  }
  .tick-badge {
    width: 80px; height: 80px;
    border-radius: 50%;
    background: var(--accent-blue);
    display: flex;
    align-items: center;
    justify-content: center;
  }
  .service-list {
    position: absolute;
    left: 39px; top: 336px;
    display: flex;
    gap: 51px;
  }
  .service-item {
    width: 80px;
    text-align: center;
  }
  .service-icon {
    width: 80px; height: 80px;
    border-radius: 50%;
    background: var(--accent-blue-dark);
    display: flex;
    align-items: center;
    justify-content: center;
  }
  .service-label {
    margin-top: 11px;
    font-size: 15px;
    line-height: 1.4;
    color: var(--ink);
    width: 120px;
    margin-left: -20px;
  }
  .coverage-note {
    position: absolute;
    left: 43px; top: 506px;
    font-size: 13px;
    line-height: 1.5;
    color: var(--muted);
  }
  .intro {
    position: absolute;
    left: 761px; top: 160px;
    width: 360px;
  }
  .intro-title {
    font-family: "Source Serif 4", Georgia, serif;
    font-weight: 600;
    font-size: 43px;
    line-height: 1.17;
    color: var(--white);
  }
  .intro-text {
    margin-top: 43px;
    width: 330px;
    font-size: 11.5px;
    line-height: 1.45;
    color: var(--para-light);
  }
  .explore-button {
    position: absolute;
    left: 762px; top: 514px;
    width: 203px; height: 44px;
    background: var(--white);
    color: var(--accent-blue-dark);
    font-size: 15px;
    display: flex;
    align-items: center;
    justify-content: center;
    text-decoration: none;
  }
</style>
</head>
<body>
  <header class="site-header">
    <div class="brand-name">bluefinch</div>
    <div class="nav-home">Home</div>
    <nav class="nav-links">
      <span>Residential</span>
      <span>Lighting</span>
    </nav>
  </header>

  <main class="content-column">
    <div class="hero-photo" role="img" aria-label="Photo of a green lawn with sprinklers watering the grass"></div>

    <div class="feature-ticks">
      <div class="tick-badge">
        <svg width="36" height="36" viewBox="0 0 36 36"><path d="M7 19 L15 27 L30 10" fill="none" stroke="#fff" stroke-width="4" stroke-linecap="round" stroke-linejoin="round"/></svg>
      </div>
      <div class="tick-badge">
        <svg width="36" height="36" viewBox="0 0 36 36"><path d="M7 19 L15 27 L30 10" fill="none" stroke="#fff" stroke-width="4" stroke-linecap="round" stroke-linejoin="round"/></svg>
      </div>
      <div class="tick-badge">
        <svg width="36" height="36" viewBox="0 0 36 36" stroke="#fff" stroke-width="3" stroke-linecap="round"><line x1="18" y1="5" x2="18" y2="31"/><line x1="6.7" y1="11.5" x2="29.3" y2="24.5"/><line x1="6.7" y1="24.5" x2="29.3" y2="11.5"/></svg>
      </div>
      <div class="tick-badge">
        <svg width="36" height="36" viewBox="0 0 36 36"><path d="M7 19 L15 27 L30 10" fill="none" stroke="#fff" stroke-width="4" stroke-linecap="round" stroke-linejoin="round"/></svg>
      </div>
    </div>

    <section class="service-list">
      <div class="service-item">
        <div class="service-icon">
          <svg width="36" height="36" viewBox="0 0 36 36" fill="none" stroke="#fff" stroke-width="2.5"><circle cx="18" cy="18" r="14"/><circle cx="18" cy="18" r="8"/></svg>
        </div>
        <div class="service-label">Smart<br>Irrigation</div>
      </div>
      <div class="service-item">
        <div class="service-icon">
          <svg width="36" height="36" viewBox="0 0 36 36" fill="none" stroke="#fff" stroke-width="2.5"><rect x="9" y="5" width="18" height="26"/><line x1="18" y1="10" x2="18" y2="26"/><line x1="14" y1="14" x2="22" y2="14"/></svg>
        </div>
        <div class="service-label">Stunning<br>Lighting</div>
      </div>
      <div class="service-item">
        <div class="service-icon">
          <svg width="36" height="36" viewBox="0 0 36 36" fill="none" stroke="#fff" stroke-width="2.5"><rect x="5" y="7" width="26" height="18"/><line x1="12" y1="30" x2="24" y2="30"/><rect x="12" y="12" width="12" height="8"/></svg>
        </div>
        <div class="service-label">Reliable<br>Service</div>
      </div>
      <div class="service-item">
        <div class="service-icon">
          <svg width="36" height="36" viewBox="0 0 36 36" fill="none" stroke="#fff" stroke-width="2.5"><rect x="8" y="5" width="20" height="26"/><line x1="12" y1="13" x2="24" y2="13"/><line x1="12" y1="19" x2="24" y2="19"/><line x1="12" y1="25" x2="20" y2="25"/></svg>
        </div>
        <div class="service-label">Local<br>Experts</div>
      </div>
    </section>

    <p class="coverage-note">Residential Commercial Service in Southern Maine<br>trusted for years</p>
  </main>

  <section class="intro">
    <h1 class="intro-title">Experience the Bluefinch Difference</h1>
    <p class="intro-text">Our crews keep every zone running, every head turning and every yard lit, with careful service from spring start up through winter so your property stays green and bright all year.</p>
  </section>

  <a class="explore-button" href="#services">Explore Services</a>
</body>
</html>
```